Tradeshow Booth, Banners & Brochure Design

Corvin Meridian (www.corvinmeridian.example) is a Veltrax Partner specializing in developing products and customizations for Veltrax Ledgerline QP. The purpose of this project is to develop a unified approach to graphic design for our tradeshow booth, banners and product literature. This should result in completed designs for the booth and banners, and several templates that can be used to create our product literature.

***WE WILL ONLY LOOK THROUGH THE FIRST 100 SUBMISSIONS***
Updates

Reason: We have received some requests for an extended deadline, and we would like to encourage more submissions, so we are extending the deadline by two days. Please let us know if you have any questions or need clarification on our design brief.

Thanks for the submissions and questions everyone.  I will get answers to your questions, and more detailed specs, posted within the next couple of hours.  I will also provide detailed feedback to your designs within that time.

Q:  How large should each item be – what is the approximate number of words/lines, columns/rows?

 

-          We have updated the Content Type list to cut it down and simplify this.  For word count, we are attaching the text for our NEW brochure on WMS, which we intend to be a 4 page brochure.  We have labeled each section according to content type.  This can be used as a guide for how much text each content area must be able to accommodate.  You can even pull the raw text straight from the word file for your design.  The CCEM brochure, already included, is an OLD brochure, and represents a design that we are trying to evolve beyond.

 

-          Keep in mind that the 4 page product brochure will be a 17” by 11” single sheet, folded.  The 2 page product brochure will be a single 8.5” by 11” sheet, printed on both sides.

 

-          For the 2 page product brochure, assume something that looks like half of the 4 page design.  For example, we will be creating one brochure for “Financials” which comprises two products.  Product A will go on the front, and Product B on the back.  We will still need to allow for contact information and the other content types as specified.

 

-          For the 4 page corporate overview, we have attached our current corporate overview for reference, and labeled the content types.  Again, feel free to pull raw text directly from this for purposes of your design – though remember, this OLD brochure represents a design we are trying to evolve beyond.

 

-          For images (screenshots, stock photography, diagrams, etc) we are thinking we would like to see about 4 on the 4 page brochure, but only 1-2 for the 2 page brochure.  The corporate overview can have suitable imagery at your discretion.

 

-          We would like to see some of the imagery used in the Tradeshow materials (booth, banners) carried across to the brochures.

 

 

 

Q:  What are the detailed print guidelines, especially in relation to bleeds, etc?

 

-          For all the brochures, use a full bleed.  If your design incorporates a bleed of color across a fold, try to have the bleed going across no more than 25% of the height of the page.  CMYK color, 300DPI, 8.5”w x 11”h.  We will most likely go with 100# paper without too much gloss on it. 

 

-          For all other materials such as booth and banners, no bleeds.  Please see specification sheets for the booth and banners, included below.  Create your designs to the exact size given.

 

 

 

Q:  Will booth graphics be printed as one continuous piece, or will they be applied in sections that are in line with the panel dimensions of the 8 center panels and end caps?

 

-          Graphics are printed as one continuous piece on a large format printer.  They are then cut into the individual panel pieces for shipping and storage.  When the booth is fully assembled, the seams are hardly noticeable unless you are looking for them from a short distance away.

 

-          We are already in possession of one 10’ booth, and will be ordering another, with the associated pieces, to create the 20’ booth.  The booth comprises a support structure, and the actual graphics panels which are attached to the front.  The overall 20’ design should take into account the fact that we will, in the future, attend tradeshows with only a 10’ booth, so only half of the panels will be used.  We would like to be able to mix and match our four categories to suit the show.

Reason: We are extending the deadline one more time to allow Tamsin and anyone else who needs the extra time for the brochure design.

Please prioritize your brochure design at this time.  We are interested in receiving feedback on deadlines - if you can confirm that you will submit a design but need more time to do so, we would like to hear from you.

Reason: To provide time for solid designs from all the designers who have been invited, we are extended the deadline one more time. This will be the final extension.

Target Market(s)

Corporate Clients

Industry/Entity Type

Graphic Design

Requirements
Must have
• TRADESHOW SPECIFIC
1. Graphics for 10'x20' “Heronfold” Tradeshow Booth
a. Layout should approximate the grid we have mocked up in our preliminary layout – see below. There is a fair amount of flexibility so long as the basic grid, contents and dimensions are adhered to.

2. Graphics needed for 3 retractable banner stands
a. Two banner stands will have dimensions of 24” x 88”
b. The third banner stand will have dimensions of 36” x 88” and will be double-sided. The design for this banner should have the option to be scaled down to 33.5” wide, for a possible additional banner stand being considered.
c. Banners should approximate what is shown in the preliminary layout – see below.
d. All banner stands being used are able to fully extend to 92”- however, the height of the booth itself is 88” and we would like all tradeshow specific elements to be the same height.

PRODUCT LITERATURE
1. Graphic Design and Layout needed for brochures:
a. double-sided one page for Products
b. double-sided two page for Products
c. double-sided two page for Overview

2. Pages would be full bleed letter size 8.5” x 11.

3. Samples are included below to get an idea of common grids and layouts for similar publications, as well as one of our current publications for reference.

4. Product literature must include provisions for all of the content types listed in that document, included below. There is some leeway with image placement – a product brochure doesn’t necessarily have to have stock photos, diagrams, AND software screenshots.

5. The designer will need to indicate what specs are required for software screenshots so that we can generate appropriate files for that use.

COMMON ELEMENTS
• Images need to include stock photos of people in business settings, as well as stock photos related to warehousing, barcoding systems, and supply chains. Other images to be used should include schematics, workflow diagrams, and other items that are related to the areas in which the company works. Each heading on the booth, and each page on the brochures, will need one image at minimum. Images and content laid out next to each other should be thematically related whenever possible. We will also create a small number of simple diagrams in house that will need to be redesigned and recreated in the appropriate format and placed in the designs.
• Clean, high-impact design. The Veltrax Tabular Bookkeeping brochure, included below, is a good example of this.
• Our current logo, included below, needs to have the tagline removed. We are also requesting that a different version of the graphic element in the logo be created, in monochrome but with roughly the same geometry.
• Our new tagline is “Integrated Solutions for Ledgerline QP” but it should not be located directly in the logo area as our current tagline is, “Making systems business-ready”.
• Designs should be produced in print-ready PDF files. We will be using Kestrel Layout Pro R4 to open the PDF files, drop in our copy and other content, and finalize the designs. The PDF files will then be sent directly to our booth production and brochure printing companies.

```html
<!DOCTYPE html>
<html lang="en">
<head>
<meta charset="utf-8">
<title>Corvin360 WMS Brochure Spread</title>
<link rel="stylesheet" href="https://fonts.googleapis.com/css2?family=Open+Sans:wght@400;600&display=swap">
<style>
:root{
  --crimson:#a30f16;
  --olive:#c3bf2f;
  --lime:#c9c63a;
  --amber:#f5b01a;
  --slate:#9aa0b4;
  --ink:#222;
  --heading-red:#a81c1c;
  --paper:#fff;
  --rule:#777;
}
*{margin:0;padding:0;box-sizing:border-box}
html,body{width:1200px;height:775px;overflow:hidden;background:var(--paper)}
body{font-family:"Open Sans",Arial,sans-serif;color:var(--ink)}
.spread{position:relative;width:1226px;height:792px;transform:scale(.9788);transform-origin:0 0;background:var(--paper);border:1px solid var(--rule)}
.abs{position:absolute}
.fold{left:611px;top:0;width:1px;height:792px;background:var(--rule)}

.accent-strip{left:42px;top:44px;width:12px;height:246px;background:var(--lime)}
.section-block{background:var(--crimson);color:#fff}
.inventory-block{left:54px;top:44px;width:136px;height:246px}
.section-tab{position:absolute;font-size:10px;font-weight:400;color:#111;padding:2px 4px;line-height:14px;white-space:nowrap;overflow:hidden}
.inventory-block .section-tab{left:1px;top:75px;width:125px;background:var(--lime)}
.block-copy{position:absolute;font-size:7.6px;line-height:10.6px}
.inventory-block .block-copy{left:5px;top:100px;width:118px}

.features-panel{left:192px;top:44px;width:377px;height:246px;background:var(--olive)}
.features-title{font-size:11px;color:var(--heading-red);font-weight:400}
.features-panel .features-title{position:absolute;left:22px;top:77px}
.feature-list{list-style:none;font-size:7.6px;line-height:10.5px}
.feature-list li{position:relative;padding-left:14px;text-align:justify;margin-bottom:10px}
.feature-list li::before{content:"•";position:absolute;left:0;top:0;font-size:9px}
.features-panel .feature-list{position:absolute;left:25px;top:101px;width:332px}

.bubble-art{left:192px;top:293px;width:377px;height:174px;
  background:radial-gradient(circle at 75% 30%,#e8f6ff 0,#8fd3ff 14%,transparent 30%),
  radial-gradient(circle at 45% 70%,#d8f0ff 0,#6cc0f5 16%,transparent 32%),
  linear-gradient(120deg,#1a5fb8,#2f8fe0 45%,#62c4f5 70%,#1c63bf)}

.label-heading{left:192px;top:482px;font-size:11px;color:var(--heading-red);font-weight:400}
.label-intro{left:192px;top:510px;width:378px;font-size:7.4px;line-height:10.5px}
.label-features{left:192px;top:556px}
.label-list{left:194px;top:579px;width:162px}
.label-list li{text-align:justify;margin-bottom:14px}
.label-list li:nth-child(3){margin-top:-8px}

.photo{left:612px;top:0;width:613px;height:792px;
  background:radial-gradient(ellipse 22% 26% at 38% 48%,#f6c7a0 0,#e9a874 60%,transparent 100%),
  radial-gradient(ellipse 40% 35% at 70% 70%,#d92a17 0,#b81a10 55%,transparent 100%),
  linear-gradient(180deg,#efe6dc 0,#e6d2b9 30%,#c98d52 60%,#e0a066 80%,#d48a4b 100%)}
.photo-band{left:995px;top:0;width:43px;height:792px;background:rgba(150,120,110,.35)}
.photo-band-top{left:995px;top:0;width:43px;height:44px;background:var(--slate)}
.photo-dash{left:1050px;top:290px;width:0;height:502px;border-left:1px dashed rgba(255,255,255,.7)}

.manufacturing-copy-panel{left:612px;top:44px;width:426px;height:246px;background:var(--paper)}
.manufacturing-copy-panel .features-title{position:absolute;left:83px;top:77px}
.manufacturing-copy-panel .feature-list{position:absolute;left:86px;top:101px;width:322px}
.manufacturing-block{left:1038px;top:44px;width:136px;height:246px}
.manufacturing-block .section-tab{left:8px;top:76px;width:128px;background:var(--amber)}
.manufacturing-block .block-copy{left:11px;top:102px;width:116px}
.amber-strip{left:1174px;top:44px;width:12px;height:246px;background:var(--amber)}
</style>
</head>
<body>
<main class="spread">
  <div class="abs accent-strip"></div>
  <section class="abs section-block inventory-block">
    <h2 class="section-tab">Inventory Management</h2>
    <p class="block-copy">Do you dread the time it takes to do an inventory stock count? With Corvin360 WMS you can not only reduce the time it takes to complete a count, but minimize the errors by using barcode scanners instead of pen and paper.</p>
  </section>
  <section class="abs features-panel">
    <h3 class="features-title">Features &amp; Benefits:</h3>
    <ul class="feature-list">
      <li>Accurate Site and Bin Tracking: Perform Site-to-Site inventory transfer or Bin-to-Bin moves while maintaining a complete log of all transfer transactions. Corvin360 WMS also supports bin transfers of items on un-posted PO Receipts so you're always "in the know".</li>
      <li>Timely Stock Counts: Process timely and relevant stock counts via barcode scanners utilizing the Stock Count Schedule in Veltrax Ledgerline QP. Warehouse supervisors can also setup Stock Count Schedules based on bin locations, sites or other filters for extreme effectiveness.</li>
    </ul>
  </section>
  <div class="abs bubble-art" role="img" aria-label="Abstract illustration of glowing blue bubbles and light streams"></div>

  <h2 class="abs label-heading">Barcode Label Printing</h2>
  <p class="abs label-intro">Do your stock items come with barcode labels that do not match your own part numbers? Or, perhaps items may come without a barcode label? You can easily create new barcoded labels to match the items you have in your Veltrax Ledgerline QP system with Corvin360 WMS.</p>
  <h3 class="abs features-title label-features">Features &amp; Benefits:</h3>
  <ul class="abs feature-list label-list">
    <li>Automatic Barcode Labeling: Barcode labels can be automatically generated within the Purchasing and Inventory modules in Veltrax Ledgerline QP from Corvin360 WMS.</li>
    <li>Proper Barcode Assignments: Barcode labels can be assigned to inventory units of measure, which allows separate label definitions for individual items, box, and pallet label types.</li>
    <li>Print Labels on the Fly: Barcode labels can be automatically generated during the receiving or picking process.</li>
  </ul>

  <div class="abs fold"></div>

  <div class="abs photo" role="img" aria-label="Photo of a smiling young woman in a red top lying on a wooden floor with friends behind her"></div>
  <div class="abs photo-band"></div>
  <div class="abs photo-band-top"></div>
  <div class="abs photo-dash"></div>

  <section class="abs manufacturing-copy-panel">
    <h3 class="features-title">Features &amp; Benefits:</h3>
    <ul class="feature-list">
      <li>Simplified Workflows: From manufacturing orders to creating a pick list, a streamlined workflow within Corvin360 WMS takes you through every step of the process for successful completion of manufacturing orders.</li>
      <li>Real-Time Manufacturing Order Updates: With the Corvin360 WMS handheld scanners, employees can pick items as well as receive MOs and the data is reflected in real time to the business office and sales personnel.</li>
    </ul>
  </section>
  <section class="abs section-block manufacturing-block">
    <h2 class="section-tab">Manufacturing</h2>
    <p class="block-copy">Manufacturing requires streamlined processes so that the right tools are used to create an optimal end product for your consumers. If you have any broken links in your chain, you could be at greater risk than you realize. With simplified workflows and real-time access to data through mobile devices, Corvin360 WMS can repair any</p>
  </section>
  <div class="abs amber-strip"></div>
</main>
</body>
</html>
```